Brightfern Studios Company Wordpress Site

We need a new company site for an established game development studio in Dallas, Texas. It should be a much more professional look than we have now, but we still want it to be a bit fun. It needs to be built so we can add more content later (as we publish new games, gain new clients, etc).
This could be built as a single page, multi-page, or a hybrid design. The design must scale to fit desktop and mobile browsers. This job will require that the website be both designed, and coded in Wordpress.
Your design should include at least the following areas:
MAIN LANDING AREA
- The company logo.
- Basic company info with a call to action.
- Twitter feed integration for news.
- Social media links.
GAMES AREA
- Section for games we have developed (logos and links).
- Second section for games we have ported (logos and links).
- This area should be designed to expand to many games.
SERVICES AREA
- Two or three paragraphs of text.
- A few images related to our services.
- FAQ about our services.
CONTACT AREA
- One or two paragraphs of text.
- Contact form.
ABOUT AREA
- Two or three paragraphs about the company.
- A few images about the company.
We will provide the final text and images to use on the site once a winning design is selected.
Again we need a more professional, modern, and more minimalist look than our current site (www.brightfernstudios-example.com), but are not opposed to something fun. We want to retain our current logo (included in the download). We know the name of the company is offbeat, but please avoid anything gross, dark, or violent, as professionalism is key. Leaning on our past projects is a good idea because we’ve worked with some very reputable game developers.
Need extra days to review
Hey everyone. We've received some fantastic submissions and want to continue working with a few of them for a little more time before making our decision. So we have extended the deadline and have also added 2nd and 3rd place rewards. Thanks to everybody who submitted!
Target Market(s)
Gamers, game professionals, developers, technology leaders, etc.
Industry/Entity Type
Games
Coding
Coded - Design and coding required
Look and feel
Each slider illustrates characteristics of the customer's brand and the style your logo design should communicate.

```html
<!DOCTYPE html>
<html lang="en">
<head>
<meta charset="utf-8">
<title>Brightfern Studios – Mobile Layout</title>
<link rel="stylesheet" href="https://fonts.googleapis.com/css2?family=Fira+Sans:wght@600&family=Montserrat:wght@400;500;700&display=swap">
<style>
  :root {
    --page-bg: #ffffff;
    --ink: #1c1c1c;
    --nav-bg: #161616;
    --panel-dark: #1b1b1c;
    --panel-black: #000000;
    --white: #ffffff;
    --muted: #d6d6d6;
    --accent: #4338f0;
    --hero-top: #1d3a55;
    --hero-mid: #14283b;
    --hero-bottom: #121416;
  }
  * { box-sizing: border-box; margin: 0; padding: 0; }
  html, body {
    width: 1200px; height: 1200px; overflow: hidden;
    background: var(--page-bg);
    font-family: "Montserrat", Arial, sans-serif;
  }
  .board { position: relative; width: 1200px; height: 1200px; }
  .board-title {
    position: absolute; top: 22px; left: 0; width: 100%;
    text-align: center;
    font-family: "Fira Sans", Arial, sans-serif;
    font-weight: 600; font-size: 32px; color: var(--ink);
  }
  .screen { position: absolute; width: 328px; overflow: hidden; color: var(--white); }

  /* Home screen */
  .screen-home { left: 36px; top: 97px; height: 655px;
    background: linear-gradient(180deg, var(--hero-top) 8%, var(--hero-mid) 45%, var(--hero-bottom) 100%); }
  .nav { height: 50px; background: var(--nav-bg); display: flex; align-items: center; justify-content: space-between; padding: 0 14px 0 16px; }
  .nav-brand { font-weight: 700; font-size: 12px; letter-spacing: 0.5px; color: var(--white); }
  .hero-title {
    position: absolute; top: 142px; left: 0; width: 100%;
    text-align: center; font-weight: 700; font-size: 37px; line-height: 48px;
    letter-spacing: 2px; text-transform: uppercase;
  }
  .hero-lead {
    position: absolute; top: 410px; left: 64px; width: 200px;
    text-align: center; font-size: 13.5px; line-height: 24px; color: var(--muted);
  }
  .btn-outline {
    position: absolute; top: 515px; left: 84px; width: 160px; height: 40px;
    border: 1.5px solid var(--accent); border-radius: 20px;
    display: flex; align-items: center; justify-content: center;
    font-size: 12px; font-weight: 500; letter-spacing: 1.8px;
  }

  /* About screen */
  .screen-about { left: 426px; top: 97px; height: 926px; background: var(--panel-dark); }
  .tag { position: absolute; top: 54px; left: 53px; width: 111px; height: 29px;
    background: var(--accent); display: flex; align-items: center; justify-content: center;
    font-size: 15px; letter-spacing: 1.5px; }
  .about-title { position: absolute; top: 100px; left: 52px; font-size: 40px; font-weight: 500;
    line-height: 45px; letter-spacing: 4px; }
  .about-copy { position: absolute; top: 218px; left: 52px; width: 226px;
    font-size: 13px; line-height: 24px; }
  .about-photo { position: absolute; left: 0; top: 463px; width: 328px; height: 463px;
    background: radial-gradient(circle at 60% 40%, #5a3b8c 0%, #2a1e4a 40%, #121018 85%); }

  /* Team screen */
  .screen-team { left: 834px; top: 98px; height: 1003px; background: var(--panel-black); text-align: center; }
  .team-title { margin-top: 8px; font-size: 24px; font-weight: 500; letter-spacing: 4px; }
  .team-lead { margin: 8px auto 0; width: 240px; font-size: 13px; line-height: 24px; }
  .team-photo { position: absolute; left: 36px; width: 256px; height: 190px; }
  .p1 { top: 158px; background: linear-gradient(135deg, #3a3a3a, #151515); }
  .p2 { top: 368px; background: linear-gradient(90deg, #e0b551 0%, #d9a944 45%, #dcd6dc 70%); }
  .p3 { top: 578px; background: linear-gradient(135deg, #6d5a52, #3d4254 60%, #7b8696); }
  .p4 { top: 787px; background: linear-gradient(180deg, #4a4f55 0%, #5b6a86 55%, #b5a243 100%); }
</style>
</head>
<body>
<div class="board">
  <h1 class="board-title">BRIGHTFERN - Mobile Layout</h1>

  <section class="screen screen-home">
    <header class="nav">
      <span class="nav-brand">BRIGHTFERN</span>
      <svg width="22" height="14" viewBox="0 0 22 14" aria-label="Menu">
        <rect y="0" width="22" height="2" fill="#fff"/>
        <rect y="6" width="22" height="2" fill="#fff"/>
        <rect y="12" width="22" height="2" fill="#fff"/>
      </svg>
    </header>
    <h2 class="hero-title">Welcome<br>to<br>Brightfern<br>Studios</h2>
    <p class="hero-lead">We really love making video games.</p>
    <a class="btn-outline">VIEW GAMES</a>
  </section>

  <section class="screen screen-about">
    <span class="tag">THE STORY</span>
    <h2 class="about-title">ABOUT<br>US</h2>
    <p class="about-copy">Brightfern Studios, LLC is a Dallas, Texas indie game studio founded in 2002, whose success has come from our passion, experienced business acuity, and deep dedication to video games of all shapes and sizes.</p>
    <div class="about-photo" role="img" aria-label="Player at a gaming tournament station under purple stage lights"></div>
  </section>

  <section class="screen screen-team">
    <h2 class="team-title">MEET OUR TEAM</h2>
    <p class="team-lead">The dedicated people that make up Brightfern.</p>
    <div class="team-photo p1" role="img" aria-label="Black and white portrait of a team member"></div>
    <div class="team-photo p2" role="img" aria-label="Portrait of a team member in a beanie and scarf against a yellow wall"></div>
    <div class="team-photo p3" role="img" aria-label="Portrait of a team member in a hat on a busy street"></div>
    <div class="team-photo p4" role="img" aria-label="Team member in glasses writing in a notebook"></div>
  </section>
</div>
</body>
</html>
```